WEBSITE DESIGN - www.brondellix.com

We need a professional and modern looking website for our business. The current website was only made tentatively and can be viewed (we expect a website MUCH better than this). It needs to be simple and non-cluttered yet look modern and sophisticated. It needs to be very easy to navigate as our tarket market is people over the age of 45. Our logo is attached below and this should be incorporated plus the colours/theme should match this. We don't mind purchasing images online if your design includes these and we like it.

Any other specific questions please enquire as we want to hear them.

Target Market(s)

over 45 age english speaking westerners

Industry/Entity Type

Business

Number of Pages Required

1 page

Requirements
Must have
• -our logo (attached).
• -page tabs as those described (tabs.. but not necessarily each of these pages completed as well although this would be nice).
• -social media logos
• Pages should include: homepage, services, pricing, about us, contact us. There should also be a payments page designed which would link with the other pages but there would be no tab for this.

```html
<!DOCTYPE html>
<html lang="en">
<head>
<meta charset="utf-8">
<title>Brondellix – Computer Solutions</title>
<link rel="stylesheet" href="https://fonts.googleapis.com/css2?family=Lato:wght@300;400;700;900&family=Open+Sans:wght@400;600;700&display=swap">
<style>
:root{
  --gold:#d9a230;
  --gold-dark:#b9851f;
  --gold-soft:#e8c374;
  --ink:#2a2a2a;
  --text:#555;
  --muted:#8a8a8a;
  --line:#e3e3e3;
  --dark:#262626;
  --black:#111;
  --slate:#2f3a48;
  --white:#fff;
  --track:#f0f0f0;
  --card-one:#4a7fb5;
  --card-two:#9aa6b2;
  --card-three:#3b3f4a;
  --card-four:#7c7c7c;
  --card-five:#f2f2f2;
}
*{box-sizing:border-box;margin:0;padding:0}
html,body{width:1200px;height:4327px;overflow:hidden}
body{font-family:"Open Sans",Arial,sans-serif;color:var(--text);background:var(--white);position:relative}
h1,h2,h3,h4{font-family:"Lato",Arial,sans-serif;font-weight:400}
.section{position:absolute;left:0;width:1200px}

/* Header */
.site-header{top:0;height:115px;background:var(--white)}
.brand{position:absolute;left:92px;top:30px;display:flex;align-items:center;gap:12px}
.brand-dot{width:38px;height:38px;border-radius:50%;background:var(--gold)}
.brand-name{font-family:"Lato",sans-serif;font-weight:700;font-size:30px;color:var(--ink)}
.top-bar{position:absolute;right:90px;top:0;height:34px;display:flex}
.top-phone{background:var(--gold);color:var(--white);font-size:14px;font-weight:600;padding:0 18px;line-height:34px}
.top-follow{background:var(--dark);color:var(--white);font-size:13px;padding:0 14px;display:flex;align-items:center;gap:8px}
.social-dot{width:18px;height:18px;border-radius:50%;background:var(--gold)}
.main-nav{position:absolute;right:90px;top:68px;display:flex;gap:58px;font-size:14px;color:var(--ink)}

/* Hero */
.hero{top:115px;height:520px;background:linear-gradient(120deg,#cfd5d8 0%,#9aa4a9 40%,#e4e1d8 70%,#7e8489 100%)}
.hero-caption{position:absolute;left:108px;top:314px}
.hero-title{display:inline-block;background:rgba(25,25,25,.82);color:var(--gold-soft);font-family:"Lato",sans-serif;font-weight:700;font-size:46px;padding:6px 18px}
.hero-sub{display:block;background:rgba(25,25,25,.7);color:var(--gold-soft);font-size:22px;font-weight:600;padding:8px 18px;width:460px}

/* Section heading */
.heading{text-align:center;font-size:32px;color:var(--ink)}

/* Why */
.why{top:665px;height:375px}
.why .heading{margin-top:10px}
.folds{position:absolute;left:100px;top:80px;width:1000px;height:270px;display:flex}
.fold{width:250px;height:270px;color:var(--white);text-align:center;padding:70px 22px 0}
.fold:nth-child(odd){background:var(--gold);clip-path:polygon(0 0,100% 8%,100% 92%,0 100%)}
.fold:nth-child(even){background:var(--gold-dark);clip-path:polygon(0 8%,100% 0,100% 100%,0 92%)}
.fold svg{width:64px;height:64px}
.fold h3{font-weight:700;font-size:20px;margin:10px 0 6px}
.fold p{font-size:12px;line-height:17px;opacity:.85}

/* Services */
.services{top:1053px;height:375px;background:linear-gradient(180deg,#3b3b3b,#2a2a2a 60%,#4a4a4a)}
.services .heading{color:var(--white);margin-top:36px;font-weight:300;font-size:34px}
.service-row{position:absolute;top:112px;left:90px;width:1020px;display:flex}
.service{width:255px;text-align:center;color:var(--white)}
.service-circle{width:108px;height:108px;border-radius:50%;background:var(--gold);margin:0 auto;display:flex;align-items:center;justify-content:center}
.service-circle svg{width:54px;height:54px}
.service h3{font-weight:700;font-size:20px;margin:16px 0 6px}
.service p{font-size:12px;line-height:17px;color:#ccc;padding:0 18px}

/* Skills */
.skills{top:1470px;height:160px}
.skill-col{position:absolute;top:0;width:470px}
.skill-col.left{left:100px}
.skill-col.right{left:630px}
.skill{height:30px;background:var(--track);margin-bottom:26px;position:relative}
.skill-fill{height:100%;background:var(--gold);color:var(--white);font-size:12px;line-height:30px;padding-left:12px;position:relative}
.skill-fill span{position:absolute;right:8px;top:0}

/* CTA */
.cta{top:1668px;height:322px;background:linear-gradient(90deg,#c99a3a,#e3b865 50%,#c79431)}
.cta-box{position:absolute;left:120px;top:82px;width:680px;height:158px;border:2px solid rgba(255,255,255,.6);padding:28px 28px}
.cta-box h2{color:var(--white);font-weight:700;font-size:31px}
.btn-light{display:inline-block;background:var(--white);color:var(--gold);font-size:14px;padding:10px 30px;margin-top:22px}
.cta-photo{position:absolute;left:826px;top:66px;width:186px;height:186px;border-radius:50%;border:6px solid var(--white);background:linear-gradient(135deg,#d9d9d9,#8d8d8d)}

/* About */
.about{top:2030px;height:220px;text-align:center}
.about .heading{font-weight:300}
.about .heading strong{font-weight:400}
.about-rule{width:280px;height:1px;background:var(--ink);margin:6px auto 0}
.about p{width:960px;margin:24px auto 0;font-size:14px;line-height:24px}
.phone-bar{display:inline-block;margin-top:14px;background:var(--gold);color:var(--white);font-size:13px;padding:8px 36px;width:612px}

/* Stats */
.stats{top:2273px;height:150px;background:var(--black);display:flex;padding:0 96px}
.stat{flex:1;text-align:center;color:var(--white);padding-top:44px}
.stat b{display:block;font-family:"Lato",sans-serif;font-size:38px;font-weight:700}
.stat span{font-size:12px;color:#ccc}

/* Testimonials */
.testimonials{top:2465px;height:180px}
.quote{position:absolute;top:0;width:460px}
.quote.left{left:100px}
.quote.right{left:630px}
.quote-box{border:1px solid var(--line);padding:16px 20px 16px 44px;font-size:12px;font-style:italic;line-height:20px;position:relative;height:88px}
.quote-box::before{content:"";position:absolute;left:16px;top:18px;width:14px;height:14px;background:var(--muted)}
.quote-person{display:flex;align-items:center;gap:14px;margin-top:-4px}
.avatar{width:86px;height:86px;border-radius:50%;background:linear-gradient(135deg,#e5d8c5,#b9a68a);border:4px solid var(--white)}
.quote-mark{width:38px;height:38px;border-radius:50%;background:#555;margin-left:-30px;margin-top:40px}
.quote-person span{font-size:13px;color:var(--ink)}

/* Pricing */
.pricing{top:2689px;height:681px;background:linear-gradient(180deg,#3a3a3a,#2c2c2c)}
.pricing .heading{color:var(--white);margin-top:34px;font-weight:300;font-size:34px}
.plans{position:absolute;top:108px;left:100px;width:1000px;display:flex;gap:60px}
.plan{width:293px;height:520px;background:var(--white);clip-path:polygon(0 0,100% 0,100% 94%,50% 100%,0 94%);text-align:center}
.plan-head{background:var(--dark);color:var(--gold);font-family:"Lato",sans-serif;font-weight:700;font-size:18px;height:52px;line-height:52px}
.plan-price{background:#f4f4f4;padding:10px 0}
.plan-price b{display:block;font-size:17px;color:var(--ink);font-weight:600}
.plan-price span{font-size:17px;color:var(--ink)}
.plan-term{display:inline-block;border:1px solid var(--line);font-size:12px;padding:4px 22px;margin:14px 0 10px}
.plan-note{font-size:12px;line-height:18px;padding:0 26px;color:var(--ink)}
.plan-feat{font-size:12px;font-weight:700;color:var(--ink);margin-top:12px}
.btn-gold{display:inline-block;background:var(--gold);color:var(--white);font-size:14px;padding:10px 26px;margin-top:22px}
.btn-dark{background:var(--dark)}

/* Payments */
.payments{top:3400px;height:205px}
.payments .heading{font-weight:300}
.pay-row{position:absolute;top:90px;left:100px;width:1000px;display:flex;justify-content:space-between;align-items:center}
.pay-card{width:142px;height:76px;border-radius:6px}
.pay-a{background:var(--card-one)}
.pay-b{background:var(--card-two)}
.pay-c{background:var(--card-three)}
.pay-d{width:100px;height:100px;border-radius:50%;background:var(--card-four)}
.pay-e{background:var(--card-five);border:1px solid var(--line)}

/* Contact form */
.contact-form{top:3606px;height:332px;background:var(--slate)}
.contact-form .heading{color:var(--white);font-weight:300;margin-top:34px}
.fields{position:absolute;top:108px;left:100px;width:1000px;display:grid;grid-template-columns:repeat(3,285px);column-gap:72px;row-gap:24px}
.field{color:#cfd5dc;font-size:13px;border-bottom:1px solid #8a96a4;padding-bottom:8px}
.submit{position:absolute;left:531px;top:268px;width:138px;height:40px;background:var(--gold);color:var(--white);text-align:center;line-height:40px;font-size:14px;font-weight:600}

/* Map & details */
.location{top:3938px;height:332px}
.map{position:absolute;left:0;top:0;width:780px;height:332px;background:linear-gradient(135deg,#a9c9e6,#cfdcc6 55%,#b7cfe3)}
.details{position:absolute;left:820px;top:22px;width:360px}
.detail{display:flex;gap:16px;margin-bottom:22px}
.detail-icon{width:38px;height:38px;border-radius:50%;background:var(--dark);flex:none;display:flex;align-items:center;justify-content:center}
.detail-icon svg{width:18px;height:18px}
.detail p{font-size:12px;line-height:19px;color:var(--ink)}

.site-footer{top:4270px;height:57px;background:var(--dark);color:#bbb;font-size:12px;text-align:center;line-height:57px}
</style>
</head>
<body>

<header class="section site-header">
  <div class="brand"><span class="brand-dot"></span><span class="brand-name">Brondellix</span></div>
  <div class="top-bar">
    <div class="top-phone">555.010.2288</div>
    <div class="top-follow">Follow us on <span class="social-dot"></span><span class="social-dot"></span><span class="social-dot"></span><span class="social-dot"></span></div>
  </div>
  <nav class="main-nav"><span>Home</span><span>About Us</span><span>Our Services</span><span>Pricing</span><span>Contact Us</span></nav>
</header>

<section class="section hero" role="img" aria-label="Photo of support staff wearing headsets working at computers">
  <div class="hero-caption">
    <h1 class="hero-title">Web Designing</h1>
    <span class="hero-sub">We Believe In Careful Planning For You</span>
  </div>
</section>

<section class="section why">
  <h2 class="heading">Why We Are The Best</h2>
  <div class="folds">
    <div class="fold">
      <svg viewBox="0 0 64 64" fill="none" stroke="#fff" stroke-width="3"><rect x="12" y="14" width="40" height="26"/><path d="M6 46h52"/></svg>
      <h3>Diagnosis &amp; Repair</h3><p>A full one stop check of your machine, fixed fast and done right for you... [ + ]</p>
    </div>
    <div class="fold">
      <svg viewBox="0 0 64 64" fill="none" stroke="#fff" stroke-width="3"><circle cx="24" cy="36" r="12"/><circle cx="42" cy="22" r="8"/></svg>
      <h3>Setup &amp; Install</h3><p>New device setup and install handled with care, no fuss at all... [ + ]</p>
    </div>
    <div class="fold">
      <svg viewBox="0 0 64 64" fill="none" stroke="#fff" stroke-width="3"><circle cx="28" cy="26" r="14"/><path d="M38 36l16 16"/></svg>
      <h3>Optimization</h3><p>You will not believe how quick your old computer can run again... [ + ]</p>
    </div>
    <div class="fold">
      <svg viewBox="0 0 64 64" fill="none" stroke="#fff" stroke-width="3"><rect x="10" y="12" width="44" height="32"/><path d="M26 52h12M32 44v8"/></svg>
      <h3>Web Designing</h3><p>We design clear websites and guide you through every step... [ + ]</p>
    </div>
  </div>
</section>

<section class="section services" role="img" aria-label="Dim photo of a workspace behind the services list">
  <h2 class="heading">Best Services</h2>
  <div class="service-row">
    <div class="service">
      <div class="service-circle"><svg viewBox="0 0 54 54" fill="none" stroke="#fff" stroke-width="3"><rect x="6" y="8" width="42" height="28"/><path d="M20 46h14M27 36v10"/></svg></div>
      <h3>Tech Support</h3><p>We make technology easier for you with instant support.</p>
    </div>
    <div class="service">
      <div class="service-circle"><svg viewBox="0 0 54 54" fill="none" stroke="#fff" stroke-width="3"><rect x="10" y="12" width="34" height="22"/><path d="M4 40h46"/></svg></div>
      <h3>Downloads</h3><p>The best apps to optimize &amp; secure your digital devices.</p>
    </div>
    <div class="service">
      <div class="service-circle"><svg viewBox="0 0 54 54" fill="none" stroke="#fff" stroke-width="3"><rect x="6" y="8" width="42" height="28"/><path d="M20 46h14M27 36v10"/></svg></div>
      <h3>Web Design</h3><p>We understand that every business owner has his...</p>
    </div>
    <div class="service">
      <div class="service-circle"><svg viewBox="0 0 54 54" fill="none" stroke="#fff" stroke-width="3"><rect x="16" y="4" width="22" height="46" rx="3"/><path d="M24 43h6"/></svg></div>
      <h3>Understand the Urgency</h3><p>We believe in careful planning for you.</p>
    </div>
  </div>
</section>

<section class="section skills">
  <div class="skill-col left">
    <div class="skill"><div class="skill-fill" style="width:95%">Awesomeness<span>95%</span></div></div>
    <div class="skill"><div class="skill-fill" style="width:98%">Flexibility<span>98%</span></div></div>
    <div class="skill"><div class="skill-fill" style="width:93%">Virus Removal<span>93%</span></div></div>
  </div>
  <div class="skill-col right">
    <div class="skill"><div class="skill-fill" style="width:100%">Support<span>100%</span></div></div>
    <div class="skill"><div class="skill-fill" style="width:97%">Software Installation<span>97%</span></div></div>
    <div class="skill"><div class="skill-fill" style="width:98%">System Setup<span>98%</span></div></div>
  </div>
</section>

<section class="section cta" role="img" aria-label="Warm gold toned office photo behind the call to action">
  <div class="cta-box">
    <h2>Call us Today for Instant Tech Support NOW!</h2>
    <span class="btn-light">Contact Now</span>
  </div>
  <div class="cta-photo" role="img" aria-label="Round photo of a support agent with a headset"></div>
</section>

<section class="section about">
  <h2 class="heading">Our Customer Our Priority <strong>Lets Say Hi..</strong></h2>
  <div class="about-rule"></div>
  <p>Brondellix was established to provide consumers with access to the sophisticated, enterprise-level IT services, support and the benefits and cost savings available to larger organisations. We provide proactive monitoring and management of customers entire IT needs. Brondellix is a growing organisation dedicated to making your PC tech support easy and accessible.</p>
  <span class="phone-bar">USA +1 555 010 4417 &nbsp; | &nbsp; UK +44 20 7946 0321 &nbsp; | &nbsp; Australia +61 2 5550 1193</span>
</section>

<section class="section stats">
  <div class="stat"><b>986</b><span>Laptops</span></div>
  <div class="stat"><b>256</b><span>Routers</span></div>
  <div class="stat"><b>867</b><span>Smart Phones</span></div>
  <div class="stat"><b>1904</b><span>Desktops</span></div>
  <div class="stat"><b>511</b><span>Tablets</span></div>
  <div class="stat"><b>2456</b><span>Software Installation</span></div>
</section>

<section class="section testimonials">
  <div class="quote left">
    <div class="quote-box">Thank you for such a support. Quality support. I'm extremely impressed. It has been one of the best experiences so pleased with Brondellix. Best.</div>
    <div class="quote-person"><div class="avatar" role="img" aria-label="Customer portrait"></div><div class="quote-mark"></div><span>- Marlene Drew</span></div>
  </div>
  <div class="quote right">
    <div class="quote-box">Thanks Brondellix. That was a huge help and exactly what I was looking for. I appreciate the help; you saved me hours of frustration right there.</div>
    <div class="quote-person"><div class="avatar" role="img" aria-label="Customer portrait"></div><div class="quote-mark"></div><span>- Tessa Valloran</span></div>
  </div>
</section>

<section class="section pricing">
  <h2 class="heading">Best Prices</h2>
  <div class="plans">
    <div class="plan">
      <div class="plan-head">Quick Fix</div>
      <div class="plan-price"><b>NZD 95</b><span>USD 60* &nbsp;I&nbsp; GBP 40*</span></div>
      <span class="plan-term">1 Month</span>
      <p class="plan-note">*The price advertised might not be the same price charged to the credit card account due to exchange rate fluctuations. This means that because we are based in New Zealand we have to convert your purchase to New Zealand dollars at the exchange rate on the day it is processed.</p>
      <p class="plan-feat">1 Month Tech Support</p><p class="plan-feat">For 1 Computer</p><p class="plan-feat">24X7 Availability</p>
      <span class="btn-gold">Order Now</span>
    </div>
    <div class="plan">
      <div class="plan-head">Starter</div>
      <div class="plan-price"><b>NZD 140</b><span>USD 90* &nbsp;I&nbsp; GBP 60*</span></div>
      <span class="plan-term">6 Month</span>
      <p class="plan-note">*The price advertised might not be the same price charged to the credit card account due to exchange rate fluctuations. This means that because we are based in New Zealand we have to convert your purchase to New Zealand dollars at the exchange rate on the day it is processed.</p>
      <p class="plan-feat">6 Month Tech Support</p><p class="plan-feat">6 Month support for the same issue</p><p class="plan-feat">24X7 Availability</p>
      <span class="btn-gold">Order Now</span>
    </div>
    <div class="plan">
      <div class="plan-head">Advance</div>
      <div class="plan-price"><b>NZD 250</b><span>USD 160* &nbsp;I&nbsp; GBP 105*</span></div>
      <span class="plan-term">1 Year</span>
      <p class="plan-note">*The price advertised might not be the same price charged to the credit card account due to exchange rate fluctuations. This means that because we are based in New Zealand we have to convert your purchase to New Zealand dollars at the exchange rate on the day it is processed.</p>
      <p class="plan-feat">1 Year Tech Support</p><p class="plan-feat">Upto 3 Computers &amp; Printers</p><p class="plan-feat">Connected Devices with Router</p>
      <span class="btn-gold btn-dark">Order Now</span>
    </div>
  </div>
</section>

<section class="section payments">
  <h2 class="heading">Payment Options:</h2>
  <div class="pay-row">
    <div class="pay-card pay-a" aria-label="Card option"></div>
    <div class="pay-card pay-b" aria-label="Card option"></div>
    <div class="pay-card pay-c" aria-label="Card option"></div>
    <div class="pay-card pay-d" aria-label="Secure checkout badge"></div>
    <div class="pay-card pay-e" aria-label="Card option"></div>
  </div>
</section>

<section class="section contact-form">
  <h2 class="heading">Drop Us a Line</h2>
  <div class="fields">
    <div class="field">First Name</div><div class="field">Last Name</div><div class="field">Country</div>
    <div class="field">E-mail</div><div class="field">Phone</div><div class="field">State</div>
    <div class="field">Street Add</div><div class="field">Zip</div><div class="field">City</div>
  </div>
  <div class="submit">Submit</div>
</section>

<section class="section location">
  <div class="map" role="img" aria-label="Street map of the office area with a location pin"></div>
  <div class="details">
    <div class="detail">
      <div class="detail-icon"><svg viewBox="0 0 18 18" fill="#fff"><path d="M4 1l3 4-2 2c1 2 3 4 5 5l2-2 4 3-2 3C7 16 2 11 1 4z"/></svg></div>
      <p>USA +1 555 010 4417<br>UK +44 20 7946 0321<br>Australia +61 2 5550 1193</p>
    </div>
    <div class="detail">
      <div class="detail-icon"><svg viewBox="0 0 18 18" fill="none" stroke="#fff" stroke-width="1.6"><rect x="2" y="4" width="14" height="10"/><path d="M2 4l7 6 7-6"/></svg></div>
      <p><b>For Query</b> - info@brondellix.com<br><b>For Billing</b> - billing@brondellix.com<br><b>For Support</b> - support@brondellix.com</p>
    </div>
    <div class="detail">
      <div class="detail-icon"><svg viewBox="0 0 18 18" fill="#fff"><path d="M9 1a5 5 0 015 5c0 4-5 11-5 11S4 10 4 6a5 5 0 015-5zm0 3a2 2 0 100 4 2 2 0 000-4z"/></svg></div>
      <p><b>Corvell Tech Services Ltd</b><br>Kestrel House Level 2<br>14 Marlow Lane<br><b>Harbourside</b><br>Wellmont 4021 New Zealand</p>
    </div>
  </div>
</section>

<footer class="section site-footer">Copyright © 2016 Brondellix | All Rights Reserved.</footer>

</body>
</html>
```